Tervolan Pty Ltd professional business card

A professional business card template using the colours from the supplied logo.
Clean crisp lines while, Modern while not being over the top.

Target Market(s)

Construction, commerical and industrial

Industry/Entity Type

Communications

Contact Information for Business Card

For a Communications, IT, Optical fibre installation company

Colors
37b8a4

```html
<!DOCTYPE html>
<html lang="en">
<head>
<meta charset="utf-8">
<title>Tervolan Pty Ltd business card</title>
<link href="https://fonts.googleapis.com/css2?family=Open+Sans:wght@400;700&display=swap" rel="stylesheet">
<style>
  :root {
    --teal: #15909f;
    --ink: #5f6266;
    --mark-grey: #6a6b6e;
    --paper: #ffffff;
    --backdrop: #e9eaeb;
  }
  * { box-sizing: border-box; margin: 0; padding: 0; }
  html, body {
    width: 1021px;
    height: 1200px;
    overflow: hidden;
    background: var(--backdrop);
    font-family: "Open Sans", Arial, sans-serif;
  }
  .card {
    position: absolute;
    left: 108px;
    width: 805px;
    height: 461px;
  }
  .card--front { top: 110px; background: var(--teal); }
  .card--back { top: 630px; background: var(--paper); }

  .brand {
    display: flex;
    align-items: center;
    gap: 18px;
    font-weight: 700;
    letter-spacing: 2px;
    line-height: 1;
  }
  .brand__dot {
    width: 22px;
    height: 22px;
    border-radius: 50%;
    background: currentColor;
  }
  .card--front .brand {
    position: absolute;
    left: 0; right: 0; top: 185px;
    justify-content: center;
    color: var(--paper);
    font-size: 86px;
  }
  .card--back .brand {
    position: absolute;
    right: 34px; top: 62px;
    color: var(--mark-grey);
    font-size: 54px;
  }
  .card--back .brand__dot { width: 16px; height: 16px; }

  .contact {
    position: absolute;
    left: 42px;
    top: 190px;
    color: var(--ink);
    font-size: 21px;
    line-height: 30px;
  }
  .contact__name {
    color: var(--teal);
    font-weight: 700;
    font-size: 29px;
    line-height: 34px;
    letter-spacing: 0.3px;
  }
  .contact__role { margin-bottom: 10px; }
  .contact__address { margin-bottom: 12px; }
  .contact__line {
    display: flex;
    align-items: center;
    gap: 8px;
  }
  .contact__icon { width: 18px; height: 18px; fill: var(--teal); flex: none; }
</style>
</head>
<body>
  <section class="card card--front" aria-label="Card front">
    <div class="brand"><span class="brand__dot"></span>TERVOLAN</div>
  </section>

  <section class="card card--back" aria-label="Card back">
    <div class="brand"><span class="brand__dot"></span>TERVOLAN</div>
    <div class="contact">
      <p class="contact__name">DANIEL ROURKE</p>
      <p class="contact__role">President</p>
      <p class="contact__address">1820 Harbor Crest Way<br>Seacliff CA 92700</p>
      <p class="contact__line">
        <svg class="contact__icon" viewBox="0 0 24 24" aria-hidden="true"><path d="M6.6 10.8c1.4 2.8 3.8 5.1 6.6 6.6l2.2-2.2c.3-.3.7-.4 1-.2 1.1.4 2.3.6 3.6.6.6 0 1 .4 1 1V20c0 .6-.4 1-1 1C10.6 21 3 13.4 3 4c0-.6.4-1 1-1h3.5c.6 0 1 .4 1 1 0 1.3.2 2.5.6 3.6.1.3 0 .7-.2 1L6.6 10.8z"/></svg>
        555-310-4827
      </p>
      <p class="contact__line">
        <svg class="contact__icon" viewBox="0 0 24 24" aria-hidden="true"><path d="M3 7l9 6 9-6v11H3z"/><path d="M3 5h18l-9 6z"/></svg>
        drourke@tervolan.com
      </p>
      <p class="contact__line">
        <svg class="contact__icon" viewBox="0 0 24 24" aria-hidden="true"><circle cx="12" cy="12" r="9"/></svg>
        www.tervolangroup.com
      </p>
    </div>
  </section>
</body>
</html>
```